Design Business Card

Make new Business card using other card as a reference. Keep the front and back business card style with new information for business. Qorlix logo and text just like the front and add email, facebook, instagram, website url all with icons like the template. The back have logo and name like template

Email: qorlixmart@[url removed, login to view]

```html
<!DOCTYPE html>
<html lang="en">
<head>
<meta charset="utf-8">
<title>Qorlix Business Card</title>
<link rel="stylesheet" href="https://fonts.googleapis.com/css2?family=Open+Sans:wght@400;600;700&display=swap">
<style>
  :root {
    --stage: #2b2c2f;
    --card-black: #0b0b0b;
    --card-white: #ffffff;
    --ink-white: #f4f4f4;
    --ink-black: #111111;
    --rule: #9a9a9a;
  }
  * { margin: 0; padding: 0; box-sizing: border-box; }
  html, body {
    width: 1200px;
    height: 900px;
    overflow: hidden;
    background: var(--stage);
    font-family: "Open Sans", sans-serif;
  }
  .canvas {
    position: relative;
    width: 1200px;
    height: 900px;
  }
  .card {
    position: absolute;
    top: 300px;
    width: 520px;
    height: 300px;
    border-radius: 22px;
    overflow: hidden;
  }

  /* Front */
  .card-front {
    left: 50px;
    background: var(--card-black);
  }
  .front-brand {
    position: absolute;
    left: 0; right: 0;
    top: 88px;
    display: flex;
    flex-direction: column;
    align-items: center;
    gap: 14px;
  }
  .brand-dot {
    width: 34px;
    height: 34px;
    border: 4px solid var(--ink-white);
    border-radius: 50%;
  }
  .brand-name {
    color: var(--ink-white);
    font-weight: 600;
    letter-spacing: 6px;
    line-height: 1;
  }
  .front-brand .brand-name { font-size: 52px; }
  .front-rule {
    position: absolute;
    left: 150px;
    width: 220px;
    top: 222px;
    height: 1px;
    background: linear-gradient(90deg, transparent, var(--rule), transparent);
  }
  .front-url {
    position: absolute;
    left: 0; right: 0;
    top: 232px;
    text-align: center;
    color: var(--ink-white);
    font-size: 17px;
    letter-spacing: 0.5px;
  }

  /* Back */
  .card-back {
    left: 630px;
    background: var(--card-white);
  }
  .back-field {
    position: absolute;
    inset: 0;
  }
  .back-brand {
    position: absolute;
    left: 34px;
    top: 34px;
    display: flex;
    align-items: center;
    gap: 12px;
  }
  .back-brand .brand-dot {
    width: 24px;
    height: 24px;
    border: 3px solid var(--ink-black);
  }
  .back-brand .brand-name {
    color: var(--ink-black);
    font-size: 38px;
    letter-spacing: 4px;
  }
  .contact {
    position: absolute;
    left: 272px;
    top: 118px;
    color: var(--ink-white);
  }
  .contact-title {
    font-size: 20px;
    font-weight: 700;
    margin-bottom: 10px;
  }
  .contact-list { list-style: none; }
  .contact-list li {
    display: flex;
    align-items: center;
    gap: 8px;
    font-size: 14px;
    line-height: 24px;
  }
  .contact-icon {
    width: 13px;
    height: 13px;
    border-radius: 50%;
    background: var(--ink-white);
    flex: none;
  }
</style>
</head>
<body>
<main class="canvas">

  <section class="card card-front" aria-label="Card front">
    <div class="front-brand">
      <span class="brand-dot"></span>
      <span class="brand-name">QORLIX</span>
    </div>
    <div class="front-rule"></div>
    <p class="front-url">www.qorlixmart.com</p>
  </section>

  <section class="card card-back" aria-label="Card back">
    <svg class="back-field" width="520" height="300" viewBox="0 0 520 300" aria-hidden="true">
      <polygon points="0,175 520,40 520,300 0,300" fill="var(--card-black)"/>
    </svg>
    <div class="back-brand">
      <span class="brand-dot"></span>
      <span class="brand-name">QORLIX</span>
    </div>
    <div class="contact">
      <h2 class="contact-title">Qorlixmart</h2>
      <ul class="contact-list">
        <li><span class="contact-icon"></span>qorlixmart@postvia.com</li>
        <li><span class="contact-icon"></span>www.friendlink.com/qorlix.shop</li>
        <li><span class="contact-icon"></span>qorlix.shop</li>
        <li><span class="contact-icon"></span>www.qorlixmart.com</li>
      </ul>
    </div>
  </section>

</main>
</body>
</html>
```